Engineering Consultants Brochure Design

We need a brochure design for our company Kestrel Ridge Systems. We are engineering consultants, who get involved in site survey all the way through to manufacture. Our main clients are from the oil and gas industry and we are best known for our computational analysis - we are leaders in the field.

We have a concept design which has all the components we are happy with, but as Engineers our artistic skills are not up to much. We would like designers to take our mock up and add more artistic flair. We are looking for a 3 page fold out design with a glued pocket where we can put individual data sheets for each of our surfaces. This is shown in the concept design attached.

The concept designs are marked as outsidesheets and insidesheets in the uploads. We really like the timeline idea which shows we are involved at all stages of the project and not just at the analysis part.
Updates

Hi, I have uploaded a pdf called Kestrel glued pocket folder. This is our mock up layout to follow to give an idea of what we are after. Thanks, Alan

Hi, I have added some more stock images to the picture library which can be used in the designs. Thanks, Alan

Target Market(s)

Engineers, project managers

Industry/Entity Type

Oil And Gas

Colors
ec2027

Requirements
Must have
• Overall:
3 pages
Triangle glued pocket, business card holder
Quality policy on the pocket
Attached are selected images which the designer can use and edit at their own discretion.

Outer sheets :
Keep current front page with Kestrel banner and energy engineering
Map on rear page and contact email address
Feature sheet with big picture and energy engineering tag line

Inner sheet
Timeline feature on the top showing our involvement from site survey and scan to installation and commissioning, with pictures on each stage.

A first inner page with our what we do text and services

A USPs page with all our key facts and figures.

Nice to have
• Map on the rear cover showing offices in Aberdeen, Houston, Dubai and Kuala Lumpur

```html
<!DOCTYPE html>
<html lang="en">
<head>
<meta charset="utf-8">
<title>Kestrel Ridge Systems – Energy Engineering Folder</title>
<link href="https://fonts.googleapis.com/css2?family=Roboto:wght@300;400;700&family=Roboto+Condensed:wght@300;400;700&display=swap" rel="stylesheet">
<style>
:root{
  --red:#ec2027;
  --orange:#f28a1f;
  --yellow:#f6cf2a;
  --ink:#3c3c3c;
  --grey:#8a8a8a;
  --paper:#ffffff;
  --stage:#f2f2f4;
}
*{margin:0;padding:0;box-sizing:border-box}
html,body{width:1200px;height:1000px;overflow:hidden;background:var(--stage)}
body{position:relative;font-family:"Roboto",Arial,sans-serif;color:var(--ink)}
.spread{position:absolute;left:48px;top:245px;width:1122px;height:500px;background:var(--paper);box-shadow:0 1px 3px rgba(0,0,0,.12)}
.panel{position:absolute;top:0;height:500px}
.panel-left{left:0;width:377px;background:linear-gradient(90deg,#fff 0,#fff 82%,#dcdcdc 100%)}
.panel-mid{left:377px;width:370px;background:linear-gradient(90deg,#f0f0f0 0,#fff 6%,#fff 90%,#e4e4e4 100%)}
.panel-right{left:747px;width:375px;background:linear-gradient(90deg,#cfcfcf 0,#fff 10%)}
.pocket{position:absolute;left:747px;top:0;width:375px;height:500px}
/* timeline */
.timeline{position:absolute;left:0;top:0;width:1122px;height:130px}
.stage{position:absolute;top:17px;width:110px;text-align:center}
.stage-pic{margin:0 auto;width:64px;height:64px;border-radius:4px}
.stage-label{margin-top:8px;font-family:"Roboto Condensed",Arial,sans-serif;font-weight:700;font-size:7.5px;line-height:9px;color:var(--ink)}
.start-tag{position:absolute;left:22px;top:104px;width:62px;height:15px;background:var(--red);color:#fff;font-family:"Roboto Condensed",Arial,sans-serif;font-weight:700;font-size:7px;line-height:15px;padding-left:8px}
.start-tag:after{content:"";position:absolute;right:-7px;top:0;border-left:7px solid var(--red);border-top:7.5px solid transparent;border-bottom:7.5px solid transparent}
.track{position:absolute;left:84px;top:111px;width:850px;height:2px;background:linear-gradient(90deg,var(--red),var(--orange) 60%,var(--yellow))}
.dot{position:absolute;top:107px;width:9px;height:9px;border-radius:50%;background:var(--red);margin-left:-4.5px}
/* left panel */
.photo{position:absolute}
.who{position:absolute;left:0;width:370px}
.who-label{position:absolute;left:0;width:84px;text-align:right;font-family:"Roboto Condensed",Arial,sans-serif;font-weight:300;font-size:8px;color:var(--ink)}
.who-label b{font-weight:400;font-size:11px}
.who-body{position:absolute;left:95px;width:160px;font-size:5.6px;line-height:7.4px;color:var(--grey)}
.who-body.intro{width:136px}
.who-body ul{list-style:none}
.who-body li:before{content:"• "}
/* middle stats */
.fact{position:absolute;border-left:1px solid #f3b08a;padding-left:10px}
.fact-num{font-family:"Roboto Condensed",Arial,sans-serif;font-weight:300;font-size:25px;line-height:26px;color:var(--red)}
.fact-txt{font-size:7px;line-height:9px;color:var(--grey);margin-top:2px}
.group-box{position:absolute;left:377px;top:285px;width:253px;height:215px;background:var(--red);color:#fff}
.group-intro{position:absolute;left:2px;top:62px;width:116px;text-align:right;font-family:"Roboto Condensed",Arial,sans-serif;font-weight:300;font-size:8px;line-height:10px}
.group-intro b{font-weight:300;font-size:10.5px;line-height:13px;white-space:nowrap}
.group-fact{position:absolute;left:136px;width:110px}
.group-num{font-family:"Roboto Condensed",Arial,sans-serif;font-weight:300;font-size:15px;line-height:16px}
.group-txt{font-size:6px;line-height:7.5px;opacity:.9}
.seabed{position:absolute;left:542px;top:133px;width:212px;height:215px}
/* right panel */
.brand{position:absolute;left:992px;top:140px;width:120px;text-align:center}
.brand-square{width:26px;height:26px;background:var(--red);margin:0 auto 6px;border:2px solid #fff}
.brand-name{font-family:"Roboto",Arial,sans-serif;font-weight:700;font-size:12px;letter-spacing:2px;color:#fff}
.brand-line{font-size:4.4px;color:#fff;border-top:1px solid #fff;margin-top:2px;padding-top:2px;letter-spacing:.2px;white-space:nowrap}
.policy{position:absolute;left:954px;top:232px;width:170px;height:95px;color:#fff}
.policy-item{position:absolute;left:0;height:26px;display:flex;align-items:center}
.policy-ring{width:26px;height:26px;border-radius:50%;border:1px dashed rgba(255,255,255,.85);margin-right:7px;display:flex;align-items:center;justify-content:center}
.policy-ring span{width:9px;height:11px;border:1px solid #fff}
.policy-text{font-family:"Roboto Condensed",Arial,sans-serif;font-size:8px;line-height:9px}
.policy-title{position:absolute;left:115px;top:39px;font-family:"Roboto Condensed",Arial,sans-serif;font-weight:700;font-size:8px;line-height:9px}
.tagline{position:absolute;left:930px;top:448px;width:170px;text-align:right;color:#fff}
.tagline-main{font-family:"Roboto Condensed",Arial,sans-serif;font-weight:300;font-size:16px;text-align:left;padding-left:17px}
.tagline-rule{height:1px;margin:4px 0 4px 17px;background:linear-gradient(90deg,#fff,var(--yellow))}
.tagline-sub{font-weight:700;font-size:6px;line-height:7.5px}
</style>
</head>
<body>
<main class="spread">
  <section class="panel panel-left"></section>
  <section class="panel panel-mid"></section>
  <section class="panel panel-right"></section>

  <svg class="pocket" viewBox="0 0 375 500" aria-hidden="true">
    <polygon points="305,0 375,0 375,500 30,500" fill="#ec2027"/>
    <path d="M270 422 a12 12 0 0 1 24 0" fill="none" stroke="#fff" stroke-width="1"/>
  </svg>

  <!-- project timeline -->
  <div class="timeline">
    <div class="stage" style="left:57px"><div class="stage-pic" role="img" aria-label="Laser scanner on tripod" style="background:linear-gradient(#bdbdbd,#6b6b6b);width:30px"></div><p class="stage-label">Site Survey<br>and Lazer Scan</p></div>
    <div class="stage" style="left:160px"><div class="stage-pic" role="img" aria-label="Green 3D pipework model" style="background:linear-gradient(#9be28a,#2fa543);height:40px;margin-top:24px"></div><p class="stage-label">Model Build</p></div>
    <div class="stage" style="left:270px"><div class="stage-pic" role="img" aria-label="Vessel analysis with stress contours" style="background:linear-gradient(90deg,#e8b04a,#4fa0d8);height:50px;margin-top:14px"></div><p class="stage-label">Analysis</p></div>
    <div class="stage" style="left:392px"><div class="stage-pic" role="img" aria-label="Concept design of a steel module" style="background:linear-gradient(#6a6a6a,#2e2e2e);height:56px;margin-top:8px"></div><p class="stage-label">Concept Design</p></div>
    <div class="stage" style="left:503px"><div class="stage-pic" role="img" aria-label="Green verification ticks" style="background:linear-gradient(#8fd46a,#2d9b3a);height:50px;margin-top:14px"></div><p class="stage-label">Standard Verification</p></div>
    <div class="stage" style="left:621px"><div class="stage-pic" role="img" aria-label="Detailed component model" style="background:linear-gradient(#3a5fd0,#1e2f8a);width:34px"></div><p class="stage-label">Detailed Design</p></div>
    <div class="stage" style="left:759px"><div class="stage-pic" role="img" aria-label="Welder at work during fabrication" style="background:linear-gradient(135deg,#6b4a3a,#1a1a22);width:96px;height:64px;border-radius:0"></div><p class="stage-label">Fabrication<br>Management</p></div>
    <div class="stage" style="left:879px"><div class="stage-pic" role="img" aria-label="Crew installing equipment on site" style="background:linear-gradient(135deg,#7a7a72,#2c2c2a);width:86px;height:64px;border-radius:0"></div><p class="stage-label">Installation &amp;<br>Commissioning Support</p></div>

    <div class="start-tag">START HERE</div>
    <div class="track"></div>
    <span class="dot" style="left:112px"></span>
    <span class="dot" style="left:215px"></span>
    <span class="dot" style="left:325px"></span>
    <span class="dot" style="left:447px"></span>
    <span class="dot" style="left:558px"></span>
    <span class="dot" style="left:676px"></span>
    <span class="dot" style="left:814px"></span>
    <span class="dot" style="left:934px"></span>
  </div>

  <!-- what we do -->
  <div class="photo" role="img" aria-label="Offshore platform silhouetted at sunset" style="left:0;top:138px;width:235px;height:117px;background:linear-gradient(#6f7fa8 0,#b8a9b8 55%,#f0b35a 72%,#2a2a30 100%)"></div>
  <div class="photo" role="img" aria-label="Wind turbine against an orange sunset sky" style="left:238px;top:138px;width:139px;height:191px;background:linear-gradient(#3a1d12 0,#c8561a 45%,#f4a02c 65%,#5a2a10 100%)"></div>

  <div class="who" style="top:270px">
    <p class="who-label">What <b>WE</b> Do</p>
    <p class="who-body intro">Kestrel provides integrated, multi-disciplinary engineering design and analysis services to clients worldwide. It is a global division of Stormgate Well Control group and Meridian Energy Services Inc. operating within the international energy industries.</p>
  </div>
  <div class="who" style="top:322px">
    <p class="who-label">Our Core <b>Activities</b></p>
    <div class="who-body" style="top:2px"><ul>
      <li>Fire &amp; blast simulation</li><li>Plume dispersion</li><li>Offshore engineering</li><li>Subsea engineering</li><li>Pipeline engineering</li><li>Emergency response engineering</li><li>Process &amp; separation simulation</li><li>Renewables engineering</li><li>Product design &amp; development</li>
    </ul></div>
  </div>
  <div class="who" style="top:397px">
    <p class="who-label">Our Core <b>Services</b></p>
    <div class="who-body" style="top:1px"><ul>
      <li>Flow assurance and thermal engineering</li><li>Multiphase flow and computational fluid dynamics (CFD)</li><li>Multi-physics simulations</li><li>Structural &amp; mechanical design engineering</li><li>Advanced structural finite element analysis (FEA)</li><li>Marine dynamics and installation engineering</li>
    </ul></div>
  </div>
  <div class="who" style="top:447px">
    <p class="who-label">Our <b>Technologies</b></p>
    <div class="who-body" style="top:1px"><ul>
      <li>Computational Fluid Dynamic (CFD)</li><li>Finite Element Analysis (FEA)</li><li>Computer Aided Engineering (CAE)</li>
    </ul></div>
  </div>

  <!-- key facts -->
  <div class="fact" style="left:409px;top:135px"><p class="fact-num">72,000</p><p class="fact-txt">Tonnes steel installed<br>in 2013</p></div>
  <div class="fact" style="left:525px;top:135px"><p class="fact-num">350,000+</p><p class="fact-txt">Total hours work as<br>engineering consultants</p></div>
  <div class="fact" style="left:409px;top:207px;border-left:none"><p class="fact-num">5,000+</p><p class="fact-txt">Successfully completed<br>projects</p></div>

  <div class="seabed" role="img" aria-label="Cutaway of seabed with offshore platforms and subsea pipelines" style="background:linear-gradient(180deg,transparent 0,transparent 14%,#9fc9c6 14%,#5aa7ae 48%,#b59c7a 60%,#6e6257 100%);clip-path:polygon(0 30%,60% 14%,100% 40%,100% 88%,62% 100%,0 84%)"></div>

  <div class="group-box">
    <p class="group-intro">A business segment of<br><b>Meridian Energy Services,</b><br>a group with</p>
    <svg style="position:absolute;left:118px;top:30px" width="20" height="155" aria-hidden="true">
      <path d="M6 1 V153 M6 1 H14 M6 44 H14 M6 99 H14 M6 153 H14 M0 77 H6" stroke="#fff" stroke-width="1" fill="none"/>
      <circle cx="6" cy="1" r="1.6" fill="#fff"/><circle cx="6" cy="44" r="1.6" fill="#fff"/><circle cx="6" cy="99" r="1.6" fill="#fff"/><circle cx="6" cy="153" r="1.6" fill="#fff"/>
    </svg>
    <div class="group-fact" style="top:20px"><p class="group-num">14,000</p><p class="group-txt">Employees</p></div>
    <div class="group-fact" style="top:63px"><p class="group-num">40%</p><p class="group-txt">Re-investment of turnover<br>into research and<br>development</p></div>
    <div class="group-fact" style="top:119px"><p class="group-num">No.1</p><p class="group-txt">Preferred design and<br>analysis consultants</p></div>
    <div class="group-fact" style="top:170px"><p class="group-num">$4 billion</p><p class="group-txt">In revenues</p></div>
  </div>

  <!-- pocket: brand and quality policy -->
  <div class="brand">
    <div class="brand-square"></div>
    <p class="brand-name">KESTREL</p>
    <p class="brand-line">A MERIDIAN ENERGY SERVICES COMPANY</p>
  </div>

  <div class="policy">
    <div class="policy-item" style="top:0"><div class="policy-ring"><span></span></div><p class="policy-text">Set the<br>Standard</p></div>
    <div class="policy-item" style="top:33px"><div class="policy-ring"><span></span></div><p class="policy-text">Encourage<br>Improvement</p></div>
    <div class="policy-item" style="top:66px"><div class="policy-ring"><span></span></div><p class="policy-text">Satisfy<br>the Customer</p></div>
    <svg style="position:absolute;left:94px;top:10px" width="14" height="72" aria-hidden="true"><path d="M2 1 Q8 1 8 10 V30 Q8 36 13 36 Q8 36 8 42 V62 Q8 71 2 71" fill="none" stroke="#fff" stroke-width="1.6"/></svg>
    <p class="policy-title">QUALITY<br>POLICY</p>
  </div>

  <div class="tagline">
    <p class="tagline-main">Energy Engineering</p>
    <div class="tagline-rule"></div>
    <p class="tagline-sub">Specialist Engineering Consultancy and<br>Analysis Services</p>
  </div>
</main>
</body>
</html>
```